Tamsel Naturopathics business card design

Using the tamsel logo designed, we would like that incorporated into a business card. A colour scheme which works with the logo and lists the following business details:

Lowen Tamsel - Naturopath
Level 1, 57 Orrick Street
Wollongong NSW
(02) 4813 7096
www.lowentamselnaturo.example

We would also like space on the back of the card for next appointment times.

Target Market(s)

Anyone looking to improve their health

Industry/Entity Type

Business

Requirements
Must have
• Tamsel Naturopathics logo, business details.
Nice to have
• Good colour schemes, attractive, eye-catching features that are easy to read.

```html
<!DOCTYPE html>
<html lang="en">
<head>
<meta charset="utf-8">
<title>Tamsel Naturopathics business card</title>
<link rel="stylesheet" href="https://fonts.googleapis.com/css2?family=Arimo:wght@400;700&display=swap">
<style>
  :root {
    --bg: #e9ecef;
    --blue-light: #2aa6de;
    --blue-mid: #1682c4;
    --blue-deep: #0d5d9e;
    --navy: #1f5c97;
    --sky: #5a9fd0;
    --card-white: #ffffff;
    --card-grey: #dcdcdc;
    --line-green: #9fc79a;
    --ink: #333333;
  }
  * { margin: 0; padding: 0; box-sizing: border-box; }
  html, body { width: 1200px; height: 900px; overflow: hidden; }
  body {
    background: var(--bg);
    font-family: "Arimo", Arial, sans-serif;
    position: relative;
  }
  .card {
    position: absolute;
    left: 300px;
    width: 600px;
    height: 343px;
    border-radius: 22px;
    box-shadow: 0 6px 18px rgba(0,0,0,0.18);
    overflow: hidden;
  }
  /* Back of card */
  .card-back {
    top: 80px;
    background: radial-gradient(circle at 40% 35%, var(--blue-light) 0%, var(--blue-mid) 45%, var(--blue-deep) 100%);
  }
  .back-brand {
    position: absolute;
    left: 70px;
    top: 130px;
    width: 320px;
    text-align: center;
    color: var(--card-white);
    font-weight: 700;
    font-size: 40px;
    line-height: 1.05;
    letter-spacing: 1px;
  }
  .back-brand .brand-sub { display: block; font-size: 22px; letter-spacing: 4px; }
  .brand-dot {
    display: block;
    width: 90px; height: 90px;
    margin: -110px auto 20px;
    border-radius: 50%;
    background: rgba(255,255,255,0.85);
  }
  .appointment {
    position: absolute;
    right: 22px;
    top: 28px;
    width: 150px;
    height: 200px;
    background: linear-gradient(180deg, var(--card-white), var(--card-grey));
    border-radius: 12px;
    writing-mode: vertical-rl;
    transform: rotate(180deg);
    padding: 14px 12px;
    display: flex;
    gap: 12px;
    color: var(--ink);
  }
  .appointment-title { font-size: 13px; }
  .appointment-field {
    flex: 1;
    border-left: 1px solid var(--line-green);
    font-size: 7px;
    text-transform: uppercase;
    padding-top: 2px;
  }
  /* Front of card */
  .card-front {
    top: 483px;
    background: linear-gradient(160deg, var(--card-white) 30%, var(--card-grey) 100%);
  }
  .front-brand {
    position: absolute;
    right: 36px;
    top: 30px;
    color: var(--navy);
    font-weight: 700;
    font-size: 22px;
    line-height: 1.1;
    text-align: center;
  }
  .front-brand .brand-sub { display: block; font-size: 11px; letter-spacing: 2px; }
  .person { position: absolute; left: 78px; top: 190px; }
  .person-name { color: var(--navy); font-weight: 700; font-size: 24px; }
  .person-role { color: var(--sky); font-weight: 700; font-size: 13px; margin-top: 12px; }
  .contact {
    position: absolute;
    left: 320px;
    top: 190px;
    list-style: none;
    color: var(--navy);
    font-size: 15px;
    line-height: 24px;
  }
  .contact li { display: flex; align-items: center; gap: 12px; }
  .contact li.indent { padding-left: 26px; }
  .contact svg { width: 14px; height: 14px; fill: var(--sky); flex: none; }
</style>
</head>
<body>
  <section class="card card-back" aria-label="Back of card">
    <div class="back-brand"><span class="brand-dot"></span>Tamsel<span class="brand-sub">Naturopathics</span></div>
    <div class="appointment">
      <div class="appointment-title">Your next appointment:</div>
      <div class="appointment-field">Name</div>
      <div class="appointment-field">Date</div>
      <div class="appointment-field">Time</div>
    </div>
  </section>

  <section class="card card-front" aria-label="Front of card">
    <div class="front-brand">Tamsel<span class="brand-sub">Naturopathics</span></div>
    <div class="person">
      <div class="person-name">Lowen Tamsel</div>
      <div class="person-role">Naturopath</div>
    </div>
    <ul class="contact">
      <li><svg viewBox="0 0 24 24"><path d="M6.6 10.8a15 15 0 0 0 6.6 6.6l2.2-2.2a1 1 0 0 1 1-.25 11.4 11.4 0 0 0 3.6.57 1 1 0 0 1 1 1V20a1 1 0 0 1-1 1A17 17 0 0 1 3 4a1 1 0 0 1 1-1h3.5a1 1 0 0 1 1 1c0 1.25.2 2.45.57 3.57a1 1 0 0 1-.25 1z"/></svg>(02) 4813 7096</li>
      <li><svg viewBox="0 0 24 24"><path d="M12 3 2 12h3v8h5v-6h4v6h5v-8h3z"/></svg>www.lowentamselnaturo.example</li>
      <li><svg viewBox="0 0 24 24"><path d="M12 2a7 7 0 0 0-7 7c0 5.25 7 13 7 13s7-7.75 7-13a7 7 0 0 0-7-7zm0 9.5A2.5 2.5 0 1 1 12 6.5a2.5 2.5 0 0 1 0 5z"/></svg>Level 1, 57 Orrick Street</li>
      <li class="indent">Wollongong NSW</li>
    </ul>
  </section>
</body>
</html>
```